Breezeway Comfort business cards design

Need a business card design for a Heating and Air Conditioning business. I need these items included.
Business name: Breezeway Comfort
Owner: Marcus Tollefsen
License # 2874590
Phone number # 555-382-4071
Email: breezewaycomfortair@mailvista.example
Sales
Service
Installation
Maintenance

Heating and Air Conditioning

Requirements
Must have
• Company name , license number , phone number , email

```html
<!DOCTYPE html>
<html lang="en">
<head>
<meta charset="utf-8">
<title>Breezeway Comfort – Business Cards</title>
<link rel="stylesheet" href="https://fonts.googleapis.com/css2?family=Lexend:wght@400;600;700&display=swap">
<style>
  :root {
    --page-bg: #f2f3f5;
    --card-bg: #ffffff;
    --brand-blue: #1f3f9e;
    --brand-red: #e8384f;
    --brand-orange: #f0763a;
    --ink: #1c2a4a;
    --faint-warm: rgba(250, 200, 150, 0.12);
    --faint-cool: rgba(150, 170, 220, 0.10);
  }
  * { box-sizing: border-box; margin: 0; padding: 0; }
  html, body {
    width: 1199px; height: 1200px; overflow: hidden;
    background: var(--page-bg);
    font-family: "Lexend", sans-serif;
  }
  .card {
    position: absolute; left: 150px; width: 897px; height: 526px;
    background: var(--card-bg); overflow: hidden;
    border: 1px solid #e3e5ea;
  }
  .card--front { top: 59px; }
  .card--back { top: 623px; }

  .decor {
    position: absolute; border-radius: 50%;
    background: radial-gradient(circle, var(--faint-cool) 0%, var(--faint-warm) 55%, transparent 75%);
  }
  .card--front .decor { left: -40px; top: -20px; width: 420px; height: 360px; }
  .card--back .decor { right: -60px; top: 10px; width: 430px; height: 500px; }

  .brand {
    position: absolute; display: flex; align-items: center; gap: 14px;
    color: var(--brand-blue); font-weight: 600; white-space: nowrap;
  }
  .brand__dot { border-radius: 50%; background: var(--brand-orange); flex: none; }
  .card--front .brand { right: 72px; top: 170px; font-size: 34px; }
  .card--front .brand__dot { width: 26px; height: 26px; }
  .card--back .brand { left: 0; right: 0; justify-content: center; top: 230px; font-size: 56px; }
  .card--back .brand__dot { width: 40px; height: 40px; }

  .contact { position: absolute; left: 63px; top: 235px; color: var(--ink); }
  .contact__name { color: var(--brand-red); font-weight: 700; font-size: 32px; letter-spacing: 0.3px; line-height: 1; }
  .contact__role { color: var(--brand-blue); font-size: 21px; margin-top: 8px; }
  .contact__list { list-style: none; margin-top: 32px; font-size: 21px; }
  .contact__list li { display: flex; align-items: center; gap: 15px; height: 41px; }
  .contact__list svg { width: 18px; height: 18px; fill: var(--brand-red); flex: none; }
  .contact__license { margin-top: 24px; padding-left: 33px; font-size: 21px; }
</style>
</head>
<body>
  <section class="card card--front">
    <div class="decor" role="img" aria-label="Faint sun and snowflake brand decoration"></div>
    <div class="brand"><span class="brand__dot"></span>Breezeway Comfort</div>
    <div class="contact">
      <h1 class="contact__name">MARCUS TOLLEFSEN</h1>
      <p class="contact__role">Owner</p>
      <ul class="contact__list">
        <li>
          <svg viewBox="0 0 24 24" aria-hidden="true"><path d="M6.6 10.8c1.4 2.8 3.8 5.1 6.6 6.6l2.2-2.2c.3-.3.7-.4 1-.2 1.1.4 2.3.6 3.6.6.6 0 1 .4 1 1V20c0 .6-.4 1-1 1C10.6 21 3 13.4 3 4c0-.6.4-1 1-1h3.5c.6 0 1 .4 1 1 0 1.3.2 2.5.6 3.6.1.3 0 .7-.2 1z"/></svg>
          <span>555-382-4071</span>
        </li>
        <li>
          <svg viewBox="0 0 24 24" aria-hidden="true"><path d="M3 5h18c.6 0 1 .4 1 1v12c0 .6-.4 1-1 1H3c-.6 0-1-.4-1-1V6c0-.6.4-1 1-1zm9 7 8-5H4z"/></svg>
          <span>breezewaycomfortair@mailvista.example</span>
        </li>
      </ul>
      <p class="contact__license">License # 2874590</p>
    </div>
  </section>

  <section class="card card--back">
    <div class="decor" role="img" aria-label="Faint sun and snowflake brand decoration"></div>
    <div class="brand"><span class="brand__dot"></span>Breezeway Comfort</div>
  </section>
</body>
</html>
```